Book title: Wildflower: The gift of stillness!

This book is called: Wildflower: The gift of stillness!

A guide to understanding the most popular types of coaching and how to find the perfect coach for you.
The coaching industry has exploded over the past few years as the demand for them has increased. With so many different types of coaches it can be intimidating and overwhelming to find the perfect one for you. To further complicate matters, you may experience times in your life when you require multiple coaches. {Book Title} aims to quite the noise and assist you in finding the perfect coach for you. In this book, you will learn more about the different types of coaching as well as meet a hand-picked selection of coaches from the most popular coaching niches. Each featured coach has provided an exercise designed to move you powerfully forward. We encourage you to work through each exercise so you may experience firsthand the power of working with these incredible coaches.

We would like a professional and simple design. See examples included. We would like to see blood orange included in the design, please see color pallets included as well.

Target Market(s)

Corporate professionals wanting to explore the various types of coaching industry

Industry/Entity Type

Coaching - Health, business, spiritual

Font styles to use
Serif

Colors
EE7325
F08F49
F5BC92
FAE3D3
FDF4ED

Requirements
Must have
• Please include book title: Wildflower, Subtitle: The gift of stillness! Name of publishing company: Silver Lantern Publishing, Spaces for 8 author names on the front of the cover- Author Name
Nice to have
• A feminine yet corporate feel.
Should not have
• We don't want it

```html
<!DOCTYPE html>
<html lang="en">
<head>
<meta charset="utf-8">
<title>Wildflower: The gift of stillness! — Book Cover</title>
<link rel="stylesheet" href="https://fonts.googleapis.com/css2?family=Tinos:ital,wght@0,400;0,700;1,700&display=swap">
<style>
  :root {
    --blood-orange: #EF7526;
    --cream: #FDF4ED;
    --ink: #000000;
    --page: #FFFFFF;
  }
  * { margin: 0; padding: 0; box-sizing: border-box; }
  html, body {
    width: 1200px;
    height: 1000px;
    overflow: hidden;
    background: var(--page);
  }
  .book-cover {
    position: absolute;
    left: 273px;
    top: 8px;
    width: 654px;
    height: 982px;
    background: var(--cream);
    border: 1px solid var(--blood-orange);
    overflow: hidden;
    font-family: "Tinos", "Times New Roman", serif;
  }
  .staircase {
    position: absolute;
    inset: 0;
    width: 100%;
    height: 100%;
  }
  .staircase polygon { fill: var(--blood-orange); }
  .title {
    position: absolute;
    left: 0;
    right: 0;
    top: 112px;
    text-align: center;
    font-weight: 700;
    font-size: 65px;
    line-height: 65px;
    color: var(--ink);
    letter-spacing: 0.5px;
  }
  .subtitle {
    position: absolute;
    left: 109px;
    color: var(--cream);
    font-weight: 400;
    white-space: nowrap;
  }
  .subtitle-lead {
    top: 694px;
    font-size: 65px;
    line-height: 65px;
  }
  .subtitle-main {
    top: 748px;
    font-size: 80px;
    line-height: 82px;
  }
  .authors {
    position: absolute;
    left: 109px;
    width: 436px;
    top: 838px;
    color: var(--cream);
  }
  .author-row {
    display: block;
    width: 600px;
    font-size: 21px;
    line-height: 22px;
    white-space: nowrap;
    transform: scaleX(0.726);
    transform-origin: left top;
  }
  .divider {
    position: absolute;
    left: 109px;
    top: 888px;
    width: 434px;
    height: 10px;
  }
  .divider line { stroke: var(--cream); stroke-width: 1.2; }
  .divider path { fill: var(--cream); }
  .tagline {
    position: absolute;
    left: 109px;
    width: 436px;
    top: 906px;
    text-align: center;
    color: var(--cream);
    font-style: italic;
    font-weight: 700;
    font-size: 13.4px;
    line-height: 16.5px;
  }
</style>
</head>
<body>
  <main class="book-cover">
    <svg class="staircase" viewBox="0 0 1145 1718" preserveAspectRatio="none" aria-hidden="true">
      <polygon points="1145,427 982,427 982,565 816,565 816,693 652,693 652,828 488,828 488,961 320,961 320,1097 157,1097 157,1232 0,1232 0,1718 1145,1718"/>
    </svg>

    <h1 class="title">WILDFLOWER</h1>

    <p class="subtitle subtitle-lead">THE GIFT OF</p>
    <p class="subtitle subtitle-main">STILLNESS!</p>

    <div class="authors">
      <span class="author-row">AUTHOR NAME • AUTHOR NAME • AUTHOR NAME • AUTHOR NAME</span>
      <span class="author-row">AUTHOR NAME • AUTHOR NAME • AUTHOR NAME • AUTHOR NAME</span>
    </div>

    <svg class="divider" viewBox="0 0 434 10" aria-hidden="true">
      <line x1="0" y1="5" x2="208" y2="5"/>
      <line x1="226" y1="5" x2="434" y2="5"/>
      <path d="M217 0 L221 5 L217 10 L213 5 Z"/>
    </svg>

    <p class="tagline">A guide to understanding the most popular types of coaching and<br>how to find the perfect one for you.</p>
  </main>
</body>
</html>
```